Redesign of 3-4 page site for professional services firm

Our site is www.kestrelvaleadvisors.com. We currently have a simple page made with HostPlumo tools. But the tools are not able to generate the look and feel we desire. We need a home page similar to current that tells a little about our company, our experience and our team. We need a second page to show details of current and past transactions we have assisted our clients with. Currently this page reads like a word document but we would like for it to present in a cleaner fashion and liven it up with some images that link to the industry served. For example, a motorcycle outline in a circle for the powersports related transactions. We would like page to introduce each member of "Our Team" and highlight their experience with a photo of each person. If there is no photo available, we would like a placeholder to be their initials in a circle that can be updated later. We would also like a contact us section whether this is a different page or part of the home page.

Target Market(s)

Retirement minded business owners

Industry/Entity Type

Professional Services

Coding

Coded - Design and coding required

Requirements
Must have
• See project description. Must include a page or section for "Current Listings" and "Recently Completed Transactions" (can be same page)

```html
<!DOCTYPE html>
<html lang="en">
<head>
<meta charset="utf-8">
<title>Kestrel Vale Advisors – Home</title>
<link href="https://fonts.googleapis.com/css2?family=Montserrat:wght@400;500;600;700;800&display=swap" rel="stylesheet">
<style>
:root{
  --green:#1fbf1f;
  --green-dark:#13a313;
  --red:#e0121b;
  --yellow:#e6e400;
  --yellow-deep:#c8d000;
  --ink:#1d1d1d;
  --muted:#555;
  --light:#f4f4f4;
  --white:#fff;
}
*{box-sizing:border-box;margin:0;padding:0}
html,body{width:1200px;height:4200px;overflow:hidden}
body{font-family:'Montserrat',sans-serif;color:var(--ink);background:var(--white);position:relative}
.abs{position:absolute}
.eyebrow{font-size:15px;font-weight:600;letter-spacing:2px;color:var(--green);text-transform:uppercase}
.section-title{font-size:46px;font-weight:600;text-transform:uppercase;letter-spacing:1px}
.btn{display:inline-block;font-size:15px;font-weight:700;text-transform:uppercase;color:#fff;padding:14px 26px;letter-spacing:.5px}
.btn-red{background:var(--red)}
.btn-green{background:var(--green)}
.btn-dark{background:#1a1a1a}

/* header */
.site-header{top:0;left:0;width:1200px;height:100px}
.brand{display:flex;align-items:center;gap:12px;font-size:34px;font-weight:600;color:var(--ink)}
.brand-mark{width:22px;height:22px;background:var(--red)}
.site-header .brand{position:absolute;left:110px;top:28px}
.nav{position:absolute;left:430px;top:40px;display:flex;gap:56px;font-size:16px;font-weight:600;text-transform:uppercase}
.nav .active{border-bottom:2px solid var(--ink);padding-bottom:4px}
.site-header .btn{position:absolute;left:920px;top:28px;padding:12px 18px;font-size:15px}

/* hero */
.hero{top:0;left:0;width:1200px;height:720px;background:linear-gradient(180deg,#fafafa,#eeeeee)}
.hero-art{left:560px;top:60px;width:560px;height:620px;background:radial-gradient(ellipse at 55% 60%,#dfe7d8 0%,#eef0ec 55%,rgba(240,240,240,0) 75%)}
.hero-bar{left:0;top:220px;width:8px;height:220px;background:var(--green)}
.hero-copy{left:110px;top:262px}
.hero-title{margin-top:20px;font-size:60px;line-height:1.08;font-weight:800;text-transform:uppercase}
.hero-title .g{color:var(--green)}
.hero .btn{margin-top:30px;font-size:14px;padding:13px 20px}

/* about */
.about{left:100px;top:660px;width:1040px;height:500px;background:linear-gradient(180deg,var(--yellow) 0%,var(--yellow-deep) 100%);text-align:center;padding:52px 110px}
.about .eyebrow{color:var(--red)}
.about .section-title{margin:10px 0 34px;color:#1c1c1c}
.about p{font-size:17px;line-height:1.7;color:#2a2a2a;margin-bottom:22px}

/* experience */
.experience{top:1220px;left:0;width:1200px;height:760px;text-align:center}
.divider{width:2px;height:60px;background:var(--green);margin:0 auto 10px}
.experience .section-title{margin-top:8px}
.diamond{position:absolute;width:380px;height:380px;display:flex;flex-direction:column;align-items:center;justify-content:center}
.diamond svg.shape{position:absolute;inset:0}
.diamond .icon{position:relative;width:76px;height:76px;border-radius:50%;display:flex;align-items:center;justify-content:center;margin-bottom:16px}
.diamond p{position:relative;width:190px;font-size:13px;line-height:1.5;color:#333}
.diamond.featured p{color:#fff}

/* team */
.team{top:1985px;left:0;width:1200px;height:640px;background:var(--light)}
.team-corner{left:0;top:0}
.team-photo{left:160px;top:120px;width:420px;height:400px;background:linear-gradient(135deg,#8ea0b3 0%,#c9d1d8 45%,#7b8794 100%);border:10px solid #fff;outline:6px solid var(--yellow)}
.team-copy{left:640px;top:120px;width:470px}
.team-copy .eyebrow{color:var(--red)}
.team-copy .section-title{margin:8px 0 20px}
.team-copy p{font-size:17px;line-height:1.65;color:#333;margin-bottom:20px}

/* testimonials */
.testimonials{top:2660px;left:0;width:1200px;height:510px;text-align:center}
.testimonials .eyebrow{color:var(--red)}
.testimonials .section-title{margin-top:8px}
.testimonials .hl{color:var(--green)}
.quote-card{position:absolute;top:180px;width:480px;height:260px;border:1px solid #ddd;padding:34px 36px;text-align:left;box-shadow:0 4px 16px rgba(0,0,0,.07)}
.quote-card p{font-size:15px;line-height:1.6;color:#444}
.quote-author{display:flex;align-items:center;gap:12px;margin-top:22px;font-weight:700;font-size:16px}
.avatar{width:34px;height:34px;border-radius:50%;background:#c9c1b5}
.quote-mark{position:absolute;right:30px;bottom:26px;font-size:60px;font-weight:800;color:var(--green);line-height:.6}
.arrow{position:absolute;top:290px}

/* contact */
.contact{top:3180px;left:0;width:1200px;height:600px;background:var(--green);overflow:hidden}
.contact-photo{left:700px;top:0;width:500px;height:600px;background:linear-gradient(135deg,#4d5a66 0%,#9aa5ae 50%,#d8dde0 100%)}
.contact-copy{left:110px;top:90px;width:470px}
.contact-copy .eyebrow{color:#fff}
.contact-copy .section-title{color:#fff;margin:6px 0 26px}
.form-row{display:flex;gap:14px;margin-bottom:14px}
.field{flex:1;height:44px;background:#fff;font-size:14px;color:#555;padding:12px 14px;display:flex;align-items:center;gap:8px}
.field.tall{height:94px;align-items:flex-start}
.field .dot{width:10px;height:10px;background:var(--green);border-radius:50%}
.contact .btn{margin-top:10px}

/* footer */
.site-footer{top:3780px;left:0;width:1200px;height:420px}
.site-footer .brand{position:absolute;left:120px;top:60px}
.socials{position:absolute;left:120px;top:150px;display:flex;gap:18px}
.socials span{width:26px;height:26px;border-radius:50%;background:#1d1d1d}
.foot-col{position:absolute;top:60px}
.foot-col h4{font-size:15px;font-weight:700;text-transform:uppercase;border-left:3px solid var(--green);padding-left:10px;margin-bottom:16px}
.foot-col li{list-style:none;font-size:14px;color:#444;margin-bottom:10px;padding-left:13px}
.foot-input{width:220px;height:42px;border:1px solid #ccc;font-size:13px;color:#888;padding:12px;margin-bottom:14px}
.copyright{position:absolute;top:330px;left:0;width:1200px;border-top:1px solid #ddd;padding-top:22px;text-align:center;font-size:13px;color:#555}
</style>
</head>
<body>

<section class="hero abs">
  <div class="hero-art abs" role="img" aria-label="Rising red, yellow and green arrows over a city skyline, symbolising business growth"></div>
  <div class="hero-bar abs"></div>
  <div class="hero-copy abs">
    <div class="eyebrow" style="color:var(--ink)">Welcome to Kestrel Vale</div>
    <h1 class="hero-title"><span class="g">Strategically</span><br>Navigating<br>Business Exits</h1>
    <a class="btn btn-red">Get Started Today</a>
  </div>
</section>

<header class="site-header abs">
  <div class="brand"><span>Kestrel Vale</span><span class="brand-mark"></span></div>
  <nav class="nav"><span class="active">Home</span><span>Business Listings</span><span>Our Team</span></nav>
  <a class="btn btn-green">Contact Us</a>
</header>

<section class="about abs">
  <div class="eyebrow">Who we are</div>
  <h2 class="section-title">About Kestrel Vale</h2>
  <p>At Kestrel Vale Advisors, our mission is to empower entrepreneurs and business owners by facilitating seamless transactions that lead to mutual success.</p>
  <p>We understand that selling or acquiring a business can be a complex and emotional journey, which is why our dedicated team of experts is here to guide you every step of the way. With a commitment to integrity, transparency, and unmatched professionalism, we strive to create a positive and rewarding experience for all our clients.</p>
</section>

<section class="experience abs">
  <div class="divider"></div>
  <div class="eyebrow">Who we are</div>
  <h2 class="section-title">Our Experience</h2>

  <div class="diamond" style="left:70px;top:170px">
    <svg class="shape" viewBox="0 0 380 380"><polygon points="190,10 370,190 190,370 10,190" fill="#fff" stroke="#ddd" stroke-width="2"/></svg>
    <div class="icon" style="background:var(--red)"><svg width="40" height="40" viewBox="0 0 40 40"><circle cx="20" cy="20" r="14" fill="none" stroke="#fff" stroke-width="3"/><path d="M13 20l5 5 9-10" fill="none" stroke="#fff" stroke-width="3"/></svg></div>
    <p>With decades of experience, our brokers have proudly assisted numerous clients in successfully navigating the intricate journey of selling their businesses.</p>
  </div>

  <div class="diamond featured" style="left:410px;top:150px">
    <svg class="shape" viewBox="0 0 380 380"><polygon points="190,10 370,190 190,370 10,190" fill="var(--green)"/></svg>
    <div class="icon" style="background:var(--yellow)"><svg width="40" height="40" viewBox="0 0 40 40"><circle cx="20" cy="14" r="7" fill="#fff"/><path d="M7 34c2-9 24-9 26 0z" fill="#fff"/></svg></div>
    <p>Our team brings a wealth of knowledge and expertise acquired through years of working closely with entrepreneurs and business owners across diverse industries.</p>
  </div>

  <div class="diamond" style="left:750px;top:170px">
    <svg class="shape" viewBox="0 0 380 380"><polygon points="190,10 370,190 190,370 10,190" fill="#fff" stroke="#ddd" stroke-width="2"/></svg>
    <div class="icon" style="background:var(--green)"><svg width="40" height="40" viewBox="0 0 40 40"><circle cx="20" cy="20" r="8" fill="none" stroke="#fff" stroke-width="3"/><circle cx="20" cy="20" r="15" fill="none" stroke="#fff" stroke-width="3" stroke-dasharray="5 4"/></svg></div>
    <p>We understand the unique challenges and complexities involved in selling a business, from valuation and marketing to negotiations and closing the deal.</p>
  </div>

  <div class="diamond" style="left:240px;top:400px">
    <svg class="shape" viewBox="0 0 380 380"><polygon points="190,10 370,190 190,370 10,190" fill="#fff" stroke="#ddd" stroke-width="2"/></svg>
    <div class="icon" style="background:var(--green)"><svg width="40" height="40" viewBox="0 0 40 40"><path d="M8 30l8-10 6 6 10-14" fill="none" stroke="#fff" stroke-width="3"/></svg></div>
    <p>Our extensive experience allows us to anticipate potential obstacles and proactively find solutions, ensuring a seamless and efficient process.</p>
  </div>

  <div class="diamond" style="left:580px;top:400px">
    <svg class="shape" viewBox="0 0 380 380"><polygon points="190,10 370,190 190,370 10,190" fill="#fff" stroke="#ddd" stroke-width="2"/></svg>
    <div class="icon" style="background:var(--red)"><svg width="40" height="40" viewBox="0 0 40 40"><path d="M20 6l4 9 10 1-8 7 3 10-9-6-9 6 3-10-8-7 10-1z" fill="#fff"/></svg></div>
    <p>We take pride in our track record of delivering exceptional results and helping our clients achieve their desired outcomes.</p>
  </div>
</section>

<section class="team abs">
  <svg class="team-corner abs" width="260" height="640" viewBox="0 0 260 640"><polygon points="0,0 200,0 0,360" fill="var(--red)"/><polygon points="0,100 140,100 0,380" fill="var(--yellow)"/></svg>
  <div class="team-photo abs" role="img" aria-label="Business advisors shaking hands across a meeting table"></div>
  <div class="team-copy abs">
    <div class="eyebrow">Meet our team</div>
    <h2 class="section-title">Our Team</h2>
    <p>Together, our team of CPAs, attorneys, real estate brokers, and financial advisors work collaboratively to provide you with a holistic approach to business transactions.</p>
    <p>With our combined knowledge and experience, we strive to ensure a smooth and successful journey for our clients, delivering exceptional results and peace of mind.</p>
    <a class="btn btn-green">Learn More</a>
  </div>
</section>

<section class="testimonials abs">
  <div class="eyebrow">Testimonials</div>
  <h2 class="section-title">What Our <span class="hl">Client</span> Says</h2>
  <svg class="arrow" style="left:30px" width="20" height="36" viewBox="0 0 20 36"><path d="M18 2L2 18l16 16" fill="none" stroke="#999" stroke-width="3"/></svg>
  <div class="quote-card" style="left:100px">
    <p>"Lorem ipsum dolor sit amet, consectetur adipiscing elit, sed do eiusmod tempor incididunt ut labore et dolore magna aliqua. Quis ipsum suspendisse ultrices gravida. Risus commodo viverra maecenas accumsan lacus vel facilisis."</p>
    <div class="quote-author"><span class="avatar"></span>Lena Ortiz</div>
    <div class="quote-mark">&rdquo;</div>
  </div>
  <div class="quote-card" style="left:620px">
    <p>"Lorem ipsum dolor sit amet, consectetur adipiscing elit, sed do eiusmod tempor incididunt ut labore et dolore magna aliqua. Quis ipsum suspendisse ultrices gravida. Risus commodo viverra maecenas accumsan lacus vel facilisis."</p>
    <div class="quote-author"><span class="avatar"></span>Marcus Hale</div>
    <div class="quote-mark">&rdquo;</div>
  </div>
  <svg class="arrow" style="left:1150px" width="20" height="36" viewBox="0 0 20 36"><path d="M2 2l16 16L2 34" fill="none" stroke="#999" stroke-width="3"/></svg>
</section>

<section class="contact abs">
  <div class="contact-photo abs" role="img" aria-label="Advisor reviewing documents on a tablet in an office"></div>
  <svg class="abs" style="left:560px;top:0" width="300" height="600" viewBox="0 0 300 600"><polygon points="0,0 300,0 140,600 0,600" fill="var(--green)"/></svg>
  <div class="contact-copy abs">
    <div class="eyebrow">Get in touch</div>
    <h2 class="section-title">Contact Us</h2>
    <div class="form-row"><div class="field"><span class="dot"></span>First Name*</div><div class="field"><span class="dot"></span>Last Name*</div></div>
    <div class="form-row"><div class="field"><span class="dot"></span>Email Address*</div></div>
    <div class="form-row"><div class="field"><span class="dot"></span>Phone*</div></div>
    <div class="form-row"><div class="field tall"><span class="dot"></span>Leave Message</div></div>
    <a class="btn btn-dark">Send Message &rsaquo;</a>
  </div>
</section>

<footer class="site-footer abs">
  <div class="brand"><span>Kestrel Vale</span><span class="brand-mark"></span></div>
  <div class="socials"><span></span><span></span><span></span><span></span></div>
  <div class="foot-col" style="left:380px"><h4>Navigation</h4><ul><li>Home</li><li>Business Listings</li><li>Our Team</li><li>Contact Us</li></ul></div>
  <div class="foot-col" style="left:580px;width:260px"><h4>Contact Us</h4><ul><li>48 Birchfield Lane, Ardmore Ridge, United States</li><li>555-014-2290</li><li>hello@kestrelvaleadvisors.com</li></ul></div>
  <div class="foot-col" style="left:880px"><h4>Sign up for updates</h4><div class="foot-input">Email address</div><a class="btn btn-red" style="font-size:13px;padding:11px 18px">Subscribe &rsaquo;</a></div>
  <div class="copyright">Copyright &copy; 2023 Kestrel Vale Advisors. All Rights Reserved.</div>
</footer>

</body>
</html>
```